Business Card Design Project

I need a business card designed with these details on the front along with the logo attached on the front.

Address - 517/ 208 Wendlebury st Pellford
Website - www.brackwoodcarvers.com.au
Email - delmar@brackwoodcarvers.com.au
Fax - 1900 417 562
Mobile - 0471390618
Telephone - 1300627059
Licence number - 864207k

```html
<!DOCTYPE html>
<html lang="en">
<head>
<meta charset="utf-8">
<title>Brackwood Carvers – Business Card</title>
<link href="https://fonts.googleapis.com/css2?family=Libre+Baskerville:wght@700&family=Questrial&display=swap" rel="stylesheet">
<style>
  :root {
    --stage: #e9e6e1;
    --paper: #ffffff;
    --paper-back: #f3ede6;
    --brown: #5a2418;
    --taupe: #b8ab9c;
    --wave-light: #ece2d8;
    --wave-mid: #e4d6c8;
    --ink: #3a2a24;
    --muted: #8c7464;
    --light-text: #ffffff;
  }
  * { margin: 0; padding: 0; box-sizing: border-box; }
  html, body { width: 1200px; height: 720px; overflow: hidden; background: var(--stage); }
  .stage { position: relative; width: 1200px; height: 720px; }

  .card {
    position: absolute; top: 200px; width: 540px; height: 310px;
    box-shadow: 0 6px 18px rgba(0,0,0,.15); overflow: hidden;
    font-family: "Questrial", "Century Gothic", sans-serif;
  }
  .card-front { left: 45px; background: var(--paper); }
  .card-back { left: 615px; background: var(--paper-back); }

  .front-bands { position: absolute; inset: 0; }

  .brand { position: absolute; left: 28px; top: 30px; display: flex; align-items: center; gap: 12px; }
  .brand-square { width: 40px; height: 40px; background: var(--taupe); }
  .brand-name {
    font-family: "Libre Baskerville", "Times New Roman", serif; font-weight: 700;
    font-size: 17px; line-height: 1.15; color: var(--ink); letter-spacing: .5px; text-transform: uppercase;
  }

  .person { position: absolute; right: 30px; top: 88px; text-align: right; }
  .person-name { font-size: 17px; color: var(--ink); }
  .person-role { font-size: 10px; color: var(--muted); font-weight: 700; margin-top: 2px; }
  .person-mobile { font-size: 10px; color: var(--muted); margin-top: 1px; display: flex; justify-content: flex-end; align-items: center; gap: 6px; }

  .address {
    position: absolute; right: 26px; top: 162px; text-align: right;
    color: var(--light-text); font-size: 11px; line-height: 1.3;
    display: flex; gap: 8px; align-items: flex-start;
  }

  .licence { position: absolute; left: 24px; top: 234px; font-size: 11px; color: var(--ink); }
  .licence span { margin-left: 10px; }

  .contacts {
    position: absolute; right: 26px; top: 216px; text-align: right;
    color: var(--light-text); font-size: 11px; line-height: 1.35;
  }
  .contact-row { display: flex; justify-content: flex-end; align-items: center; gap: 10px; }
  .contact-row .icon { width: 10px; height: 10px; }
  .contact-web { margin-top: 18px; }
  .contact-web .contact-row { gap: 0; }

  .back-texture { position: absolute; inset: 0; }
  .back-name {
    position: absolute; left: 0; right: 0; top: 118px; text-align: center;
    font-family: "Libre Baskerville", "Times New Roman", serif; font-weight: 700;
    font-size: 38px; color: var(--brown); letter-spacing: 1px;
  }
</style>
</head>
<body>
<main class="stage">

  <section class="card card-front" aria-label="Business card front">
    <svg class="front-bands" viewBox="0 0 540 310" width="540" height="310" aria-hidden="true">
      <polygon points="0,232 315,203 540,203 540,310 0,310" fill="var(--taupe)"/>
      <polygon points="285,155 540,155 540,203 315,203" fill="var(--brown)"/>
    </svg>

    <div class="brand">
      <div class="brand-square"></div>
      <div class="brand-name">Brackwood<br>Carvers</div>
    </div>

    <div class="person">
      <div class="person-name">Delmar Ostrander</div>
      <div class="person-role">Managing Director</div>
      <div class="person-mobile">047 139 0618
        <svg width="8" height="10" viewBox="0 0 8 10" aria-hidden="true"><rect x="1" y="0.5" width="6" height="9" rx="1" fill="none" stroke="var(--ink)"/><rect x="3" y="7.2" width="2" height="1" fill="var(--ink)"/></svg>
      </div>
    </div>

    <div class="address">
      <div>517/208 Wendlebury St<br>Pellford NSW 2750,<br>Australia</div>
      <svg width="10" height="13" viewBox="0 0 10 13" aria-hidden="true"><path d="M5 0.5a4 4 0 0 1 4 4c0 3-4 8-4 8s-4-5-4-8a4 4 0 0 1 4-4z" fill="var(--light-text)"/><circle cx="5" cy="4.5" r="1.5" fill="var(--brown)"/></svg>
    </div>

    <div class="licence">Licence#<span>864207k</span></div>

    <div class="contacts">
      <div class="contact-row">130 062 7059
        <svg class="icon" viewBox="0 0 10 10" aria-hidden="true"><path d="M2 1l2 2-1 1.2a6 6 0 0 0 2.8 2.8L7 6l2 2-1.2 1.2C4.5 9 1 5.5.8 2.2z" fill="var(--light-text)"/></svg>
      </div>
      <div class="contact-row">1900 417 562
        <svg class="icon" viewBox="0 0 10 10" aria-hidden="true"><rect x="1" y="4" width="8" height="5" fill="var(--light-text)"/><rect x="3" y="1" width="4" height="3" fill="none" stroke="var(--light-text)"/></svg>
      </div>
      <div class="contact-row">delmar@brackwoodcarvers.com.au
        <svg class="icon" viewBox="0 0 10 10" aria-hidden="true"><rect x="0.5" y="2" width="9" height="6" fill="var(--light-text)"/><path d="M0.5 2l4.5 3.5L9.5 2" fill="none" stroke="var(--taupe)"/></svg>
      </div>
      <div class="contact-row">www.brackwoodcarvers.com.au
        <svg class="icon" viewBox="0 0 10 10" aria-hidden="true" style="margin-left:10px"><circle cx="5" cy="5" r="4.2" fill="none" stroke="var(--light-text)"/><path d="M0.8 5h8.4M5 0.8c-2 2.5-2 5.9 0 8.4M5 0.8c2 2.5 2 5.9 0 8.4" fill="none" stroke="var(--light-text)" stroke-width=".7"/></svg>
      </div>
    </div>
  </section>

  <section class="card card-back" aria-label="Business card back">
    <svg class="back-texture" viewBox="0 0 540 310" width="540" height="310" role="img" aria-label="Soft stone-grain wave texture">
      <defs>
        <linearGradient id="stoneGrain" x1="0" y1="0" x2="1" y2="1">
          <stop offset="0" stop-color="var(--wave-mid)"/>
          <stop offset="1" stop-color="var(--paper-back)"/>
        </linearGradient>
      </defs>
      <rect x="0" y="0" width="300" height="310" fill="url(#stoneGrain)" opacity=".8"/>
    </svg>
    <div class="back-name">Brackwood Carvers</div>
  </section>

</main>
</body>
</html>
```